Professional violinist needs business cards

I am trying to attract the following jobs:
-private violin lessons (primarily classical)
-performance gigs (weddings, birthday parties, funerals, etc.)
-collaborations with other artists (studio recordings, performances)

I want to communicate that I have a very high standard of excellence for my work, but I also love people and celebrations.
Values/style words I like are:
love, joy, peace, fun, beauty, authenticity, excellence, warmth, refined/sleek, free spirited. If that's too confusing, just ignore :)

I will attach my favorite business card template that I could find on Canva. The lines are supposed to be like a music staff, which I think is really cool, but I also don't want it to look too busy. I like the simple black and white--I think it looks sharp--but I also am open to other ideas. I also have seen business cards with pictures included that looked great, so I attached an image that could be used as well.

I am also attaching a file that I made of my initials that could be used as a logo, but I'm not sure if it should be included.

Information on the card:
-My name (18 letters total)
-"violinist"
-phone number, email, website

Thank you!

```html
<!DOCTYPE html>
<html lang="en">
<head>
<meta charset="UTF-8">
<title>Elena Marwood – Violinist Business Cards</title>
<link rel="stylesheet" href="https://fonts.googleapis.com/css2?family=Open+Sans:wght@400;700&family=Questrial&display=swap">
<style>
  :root {
    --backdrop: #3b3b3d;
    --card: #242424;
    --ink: #ffffff;
    --ink-soft: #e6e6e6;
    --photo-stone: #6f6659;
    --photo-dark: #2b2622;
  }
  * { box-sizing: border-box; margin: 0; padding: 0; }
  html, body {
    width: 1200px;
    height: 900px;
    overflow: hidden;
    background: var(--backdrop);
  }
  .canvas {
    position: relative;
    width: 1200px;
    height: 900px;
  }
  .card {
    position: absolute;
    width: 630px;
    height: 360px;
    background: var(--card);
    border-radius: 26px;
    overflow: hidden;
    color: var(--ink);
    box-shadow: 0 10px 28px rgba(0,0,0,0.45);
  }
  .card--back { left: 60px; top: 60px; }
  .card--front { left: 510px; top: 480px; }

  .staff-line {
    position: absolute;
    left: 0;
    right: 0;
    height: 1px;
    background: var(--ink-soft);
  }
  .staff-line--bold { height: 3px; background: var(--ink); }

  .brand-name {
    position: absolute;
    height: 36px;
    font-family: "Open Sans", sans-serif;
    font-weight: 400;
    font-size: 26px;
    line-height: 36px;
    color: var(--ink);
    display: flex;
    align-items: center;
    gap: 10px;
    white-space: nowrap;
  }
  .brand-name__dot {
    width: 12px;
    height: 12px;
    border-radius: 50%;
    background: var(--ink);
  }

  /* back side */
  .card--back .brand-name { right: 40px; top: 102px; }
  .service {
    position: absolute;
    left: 44px;
    font-family: "Open Sans", sans-serif;
    line-height: 1.15;
  }
  .service__title { font-weight: 700; font-size: 19px; }
  .service__detail { font-weight: 400; font-size: 15px; color: var(--ink-soft); }

  /* front side */
  .portrait {
    position: absolute;
    left: 0;
    top: 110px;
    width: 250px;
    height: 250px;
    background: linear-gradient(160deg, var(--photo-stone) 0%, #4e473f 45%, var(--photo-dark) 100%);
  }
  .card--front .staff-line { left: 250px; }
  .card--front .staff-line--top { left: 0; }
  .card--front .brand-name { left: 290px; top: 57px; }
  .identity {
    position: absolute;
    left: 300px;
    top: 190px;
  }
  .identity__name {
    font-family: "Open Sans", sans-serif;
    font-weight: 700;
    font-size: 24px;
    line-height: 28px;
  }
  .identity__role {
    font-family: "Questrial", sans-serif;
    font-size: 17px;
    line-height: 20px;
  }
  .contact {
    position: absolute;
    left: 300px;
    top: 258px;
    font-family: "Questrial", sans-serif;
    font-size: 16px;
    list-style: none;
  }
  .contact__item {
    display: flex;
    align-items: center;
    gap: 8px;
    height: 24px;
    white-space: nowrap;
  }
  .contact__icon { width: 18px; height: 18px; flex: none; }
  .website {
    position: absolute;
    left: 326px;
    top: 328px;
    font-family: "Questrial", sans-serif;
    font-size: 16px;
    line-height: 22px;
    white-space: nowrap;
  }
</style>
</head>
<body>
<main class="canvas">

  <section class="card card--back" aria-label="Business card back">
    <div class="staff-line" style="top:30px"></div>
    <div class="staff-line" style="top:90px"></div>
    <div class="staff-line" style="top:150px"></div>
    <div class="staff-line" style="top:210px"></div>
    <div class="staff-line staff-line--bold" style="top:270px"></div>
    <div class="staff-line" style="top:330px"></div>

    <div class="brand-name"><span class="brand-name__dot"></span>Marwood Strings</div>

    <div class="service" style="top:162px">
      <p class="service__title">Private violin lessons</p>
      <p class="service__detail">(primarily classical)</p>
    </div>
    <div class="service" style="top:222px">
      <p class="service__title">Performance gigs</p>
      <p class="service__detail">(weddings, birthday parties, funerals, etc.)</p>
    </div>
    <div class="service" style="top:283px">
      <p class="service__title">Collaborations with other artists</p>
      <p class="service__detail">(studio recordings, performances)</p>
    </div>
  </section>

  <section class="card card--front" aria-label="Business card front">
    <div class="staff-line staff-line--top" style="top:40px"></div>
    <div class="staff-line" style="top:110px"></div>
    <div class="staff-line" style="top:180px"></div>
    <div class="staff-line staff-line--bold" style="top:250px"></div>
    <div class="staff-line" style="top:320px"></div>

    <div class="portrait" role="img" aria-label="Photo of the violinist in a black dress holding her violin and bow beside a stone wall"></div>

    <div class="brand-name"><span class="brand-name__dot"></span>Marwood Strings</div>

    <div class="identity">
      <p class="identity__name">Elena Marwood</p>
      <p class="identity__role">Violinist</p>
    </div>

    <ul class="contact">
      <li class="contact__item">
        <svg class="contact__icon" viewBox="0 0 18 18" aria-hidden="true">
          <rect x="1" y="1" width="16" height="16" rx="2" fill="none" stroke="#fff" stroke-width="1.5"/>
          <path d="M6 4.5c-1 .5-1.5 1.5-1 3 .8 2.4 2.8 4.6 5 5.5 1.4.5 2.5 0 3-1l-1.8-1.6-1.2.9c-1.2-.6-2.300-1.8-2.9-3l.9-1.2z" fill="#fff"/>
        </svg>
        <span>044-555 218 640</span>
      </li>
      <li class="contact__item">
        <svg class="contact__icon" viewBox="0 0 18 18" aria-hidden="true">
          <rect x="1" y="4" width="16" height="11" fill="#fff"/>
          <path d="M1 4l8 6 8-6" fill="none" stroke="#242424" stroke-width="1.4"/>
        </svg>
        <span>hello@elenamarwood.com</span>
      </li>
    </ul>

    <p class="website">www.elenamarwood.com</p>
  </section>

</main>
</body>
</html>
```